Flyer for GIS workshop

We need a 2 page flyer for a technology workshop for non-techies. The participants will be older farmers, land and agriculture business owners who are not tech savvy.

A bonus will be awarded to the designer that thinks of a catchy name for the workshop

Please see the following doc for the text. Some words may change but not the number of words.

https://files.plovarek.net/doc/8c2Rt5WmqZx0HvBnd7KLpYeQa3SuJfoE4iGc61Tw/view?mode=share

I have attached the organisation logo.

The organisation website is www.telbrano.org , please have a look at our old flyers (this is not professional design, we expect a lot better from participants). The new website is professionally designed and the flyer needs to have a complimentary concept.

FINAL OUTPUT
1. We need this in any opensource design software -it just needs to be free for commercial use. Some options are Scribus, Inkscape, GIMP etc.
2. All images used must be creative commons
3. The front page must be able to be used without the back (we will print this at A3 or bigger for pasting on walls)

IMPORTANT
Selected designer will be asked to work on future layouts for multiple events held every few months.

Target Market(s)

The participants will be older farmers, land and agriculture business owners who are not tech savvy.

Industry/Entity Type

Agriculture

Requirements
Must have
• Final product in any opensource design software -it just needs to be free for commercial use. Some options are Scribus, Inkscape, GIMP etc.
2 pages A4
Front page must be able to be printed at larger size and placed in shop windows or reduced in size for newspapers with minimal re-design
Nice to have
• Include Creative Common images

```html
<!DOCTYPE html>
<html lang="en">
<head>
<meta charset="utf-8">
<title>Telbrano GIS Weekend Workshop Flyer</title>
<link href="https://fonts.googleapis.com/css2?family=Alfa+Slab+One&family=Titan+One&family=Varela+Round&display=swap" rel="stylesheet">
<style>
  :root {
    --green-dark: #1f6b2e;
    --green: #2f8a3c;
    --green-light: #6fbf3a;
    --green-pale: #cfe6c4;
    --sky-top: #c9d6de;
    --sky-bottom: #f4f6f6;
    --paper: #ffffff;
    --stage: #ececec;
    --ink-white: #ffffff;
  }
  * { box-sizing: border-box; margin: 0; padding: 0; }
  html, body { width: 1200px; height: 1000px; overflow: hidden; }
  body { background: var(--stage); position: relative; font-family: "Varela Round", sans-serif; }

  .flyer {
    position: absolute; left: 250px; top: 5px;
    width: 700px; height: 990px;
    background: var(--paper);
    overflow: hidden;
    box-shadow: 0 4px 18px rgba(0,0,0,.18);
  }
  .flyer__backdrop {
    position: absolute; left: 0; top: 0; width: 700px; height: 560px;
    background: linear-gradient(180deg, var(--sky-top) 0%, #dfe6ea 45%, var(--sky-bottom) 100%);
  }
  .flyer__waves { position: absolute; left: 0; top: 0; width: 700px; height: 990px; }

  .brand {
    position: absolute; left: 0; right: 0; top: 48px;
    display: flex; justify-content: center; align-items: center; gap: 18px;
  }
  .brand__name {
    font-family: "Titan One", sans-serif; font-size: 70px; line-height: 1;
    color: var(--green); letter-spacing: 1px;
  }
  .brand__dot { width: 58px; height: 58px; border-radius: 50%; background: var(--green); }

  .questions { position: absolute; left: 28px; right: 28px; top: 180px; list-style: none; }
  .questions__item {
    height: 40px; margin-bottom: 12px;
    border: 3px solid var(--green); border-radius: 20px;
    background: rgba(255,255,255,.35);
    display: flex; align-items: center; justify-content: center;
    font-family: "Titan One", sans-serif; font-size: 12.5px; letter-spacing: 1.2px;
    text-transform: uppercase; color: var(--ink-white);
    -webkit-text-stroke: 0.6px var(--green-dark);
    text-shadow: 0 0 2px var(--green-dark);
  }

  .intro {
    position: absolute; left: 40px; right: 40px; top: 452px;
    text-align: center; font-size: 20px; line-height: 1.35;
    font-style: italic; color: var(--green);
  }
  .cta {
    position: absolute; left: 0; right: 0; top: 528px;
    text-align: center; font-family: "Alfa Slab One", serif;
    font-size: 64px; letter-spacing: 3px; color: var(--green);
    text-shadow: 0 2px 0 var(--green-dark);
  }
  .cta-sub {
    position: absolute; left: 110px; right: 110px; top: 618px;
    text-align: center; font-size: 15px; line-height: 1.3; font-weight: 700;
    font-style: italic; color: var(--green-dark); text-transform: uppercase;
  }

  .photo {
    position: absolute; left: 355px; top: 655px; width: 345px; height: 200px;
    background: linear-gradient(135deg, #b07a5c 0%, #3a3a3a 35%, #5f8fa6 60%, #2a2a2a 85%, #a06f52 100%);
    border-radius: 18px 0 0 0;
  }
  .details {
    position: absolute; left: 18px; top: 745px; width: 330px;
    text-align: center; font-size: 15.5px; line-height: 1.45;
    font-style: italic; color: var(--green-dark);
  }
  .mushrooms {
    position: absolute; background: linear-gradient(180deg, var(--green-light), var(--green));
    border-radius: 40px 40px 0 0;
  }
  .mushrooms--left { left: 10px; top: 858px; width: 150px; height: 62px; }
  .mushrooms--right { left: 560px; top: 835px; width: 140px; height: 85px; }

  .footer {
    position: absolute; left: 0; bottom: 0; width: 700px; height: 70px;
    background: var(--green-dark);
    display: flex; align-items: center; justify-content: center;
    font-size: 19px; letter-spacing: 1px; color: var(--ink-white);
  }
</style>
</head>
<body>
  <article class="flyer">
    <div class="flyer__backdrop" role="img" aria-label="Faint world map with grid lines on a pale blue-grey sky"></div>

    <svg class="flyer__waves" viewBox="0 0 700 990" aria-hidden="true">
      <path d="M0 60 C180 10 420 0 700 70 L700 0 L0 0 Z" fill="#ffffff" opacity=".55"/>
      <path d="M0 75 C200 20 430 30 700 160" fill="none" stroke="#2f8a3c" stroke-width="7"/>
      <path d="M0 95 C220 45 460 60 700 190" fill="none" stroke="#6fbf3a" stroke-width="4"/>
      <path d="M0 690 C120 690 230 720 360 770 L360 760 C230 705 120 675 0 672 Z" fill="#2f8a3c"/>
      <path d="M0 705 C140 705 240 735 360 790" fill="none" stroke="#6fbf3a" stroke-width="3"/>
      <path d="M0 650 C120 660 240 700 360 750" fill="none" stroke="#cfe6c4" stroke-width="2"/>
      <rect x="0" y="915" width="700" height="8" fill="#2f8a3c"/>
    </svg>

    <header class="brand">
      <span class="brand__name">Telbrano</span>
      <span class="brand__dot"></span>
    </header>

    <ul class="questions">
      <li class="questions__item">Do you want to visualise your agricultural environment and workflows?</li>
      <li class="questions__item">Do you want to reduce your inputs and increase your yields?</li>
      <li class="questions__item">Have you heard of geographical information systems (GIS)?</li>
      <li class="questions__item">Do you think to use a GIS will cost you lots of $$$?</li>
      <li class="questions__item">How about only $350 to learn how to in a weekend?</li>
    </ul>

    <p class="intro">You will go away with enough practical knowledge to create maps yourself and with information on how you can get more done by applying spatial techniques.</p>

    <h1 class="cta">JOIN US NOW!</h1>
    <p class="cta-sub">And get on the road to technology that will improve your productivity!</p>

    <div class="photo" role="img" aria-label="Photo of two hands holding a tablet showing a GPS map"></div>

    <p class="details">The Far North Telbrano User Group (TELBRANO) is organising a weekend program at Brackenhill Station near Corvale from 28th to 30th of November 2014.</p>

    <div class="mushrooms mushrooms--left" role="img" aria-label="Green mushroom silhouettes"></div>
    <div class="mushrooms mushrooms--right" role="img" aria-label="Green mushroom silhouettes"></div>

    <footer class="footer">www.telbrano.org/workshops/XXXX</footer>
  </article>
</body>
</html>
```